Weight loss surgery restaurant card

We need to create a card for patients who have undergone weight loss surgery to take to restaurants so they can request smaller meals. These patients have had surgery on their stomach so that they can only consume half to one cup of food at a time. So normal sized restaurant meals are way too big (and cost a lot). This card they can present to the restaurant to communicate the fact that they have had weight loss surgery and therefore request a smaller meal portion at reduced cost

Target Market(s)

Restaurants serving weight loss surgery patients

Industry/Entity Type

Health Care

Contact Information for Business Card

This will be a plastic card similar to business card size.

Requirements
Must have
• The front of the card should include the following text:
• The individual bearing this card has undergone weight loss surgery.
• This surgery restricts portion sizes to between half and one cup of food at a time.
• Please give consideration to allowing smaller portions of your regular meals to be ordered to reduce wastage and excess costs.
• Example: a half size portion priced at two thirds of usual cost.
• The back of the card will have spaces for the person to write certain information. These are the categories that can be filled in by hand:
• Name:
• Procedure performed:
• Date of procedure (month/year):
• Treating Clinic Name:
• Treating Clinic Signature:
• Somewhere down the bottom should be something along the lines of:
• supplied from bernardwhitlow.com.au
Nice to have
• A nice design with imagery/colours etc ... not just the text on a white background! Bright attractive colours preferred.
• I have uploaded my logo ... a roughly triangular image followed by my name etc. The triangular logo image could be used somewhere on the card and this logo can be interchangeable for other clinics who purchase the card.
• **Please note that I don't want my name to be included as part of the logo on the card ... just use the triangular image on the side of the logo without the following name**
• Also, the colouring of the card does not have to reflect my logo colours as I am anticipating interchanging this logo with other logos if other clinics choose to adopt the card. I am interested to see other, more generic, colour choices as well as my logo colours

```html
<!DOCTYPE html>
<html lang="en">
<head>
<meta charset="utf-8">
<title>Weight Loss Surgery Restaurant Card</title>
<link rel="stylesheet" href="https://fonts.googleapis.com/css2?family=Marcellus+SC&family=Open+Sans:wght@400&family=Marcellus&display=swap">
<style>
  :root {
    --teal: #13968c;
    --teal-dark: #0f8279;
    --paper: #f7f7f6;
    --ink: #3b3b3b;
    --white: #ffffff;
    --backdrop: #3a3432;
  }
  * { box-sizing: border-box; margin: 0; padding: 0; }
  html, body { width: 1200px; height: 844px; overflow: hidden; }
  body {
    background: var(--backdrop);
    position: relative;
    font-family: "Open Sans", Arial, sans-serif;
  }
  .card {
    position: absolute;
    top: 252px;
    width: 540px;
    height: 340px;
    border-radius: 4px;
    overflow: hidden;
    display: flex;
    box-shadow: 0 10px 30px rgba(0,0,0,0.45);
  }
  .card--back { left: 40px; background: var(--paper); }
  .card--front { left: 620px; background: var(--teal); }

  /* Back: fill-in side */
  .supplier-band {
    width: 84px;
    background: var(--teal);
    color: var(--white);
    display: flex;
    align-items: center;
    justify-content: center;
  }
  .supplier-band__text {
    writing-mode: vertical-rl;
    transform: rotate(180deg);
    text-align: left;
    line-height: 1.45;
  }
  .supplier-band__lead { font-size: 17px; font-family: "Open Sans", Arial, sans-serif; }
  .supplier-band__url { font-size: 16px; font-family: "Marcellus SC", Georgia, serif; letter-spacing: 0.5px; }

  .details {
    flex: 1;
    padding: 56px 30px 0 36px;
    list-style: none;
  }
  .details__field {
    font-family: "Marcellus SC", Georgia, serif;
    font-size: 21px;
    color: var(--ink);
    letter-spacing: 0.8px;
    line-height: 1;
    margin-bottom: 23px;
  }

  /* Front: message side */
  .clinic-strip {
    width: 88px;
    background: var(--white);
    display: flex;
    flex-direction: column;
    align-items: center;
    justify-content: space-between;
    padding: 22px 0 24px;
  }
  .clinic-strip__name {
    writing-mode: vertical-rl;
    font-family: "Marcellus", Georgia, serif;
    font-size: 26px;
    letter-spacing: 1px;
    color: var(--teal);
  }
  .clinic-strip__dot {
    width: 34px;
    height: 34px;
    border-radius: 50%;
    background: var(--teal);
  }
  .message {
    flex: 1;
    list-style: none;
    padding: 26px 26px 0 24px;
    color: var(--white);
  }
  .message__point {
    position: relative;
    padding-left: 16px;
    font-size: 12.5px;
    line-height: 1.5;
    text-transform: uppercase;
    letter-spacing: 0.2px;
    margin-bottom: 9px;
  }
  .message__point::before {
    content: "";
    position: absolute;
    left: 0;
    top: 5px;
    width: 8px;
    height: 8px;
    border-radius: 50%;
    background: var(--white);
  }
</style>
</head>
<body>
  <section class="card card--back" aria-label="Card reverse: patient details">
    <div class="supplier-band">
      <p class="supplier-band__text">
        <span class="supplier-band__lead">Purchased through</span><br>
        <span class="supplier-band__url">www.bernardwhitlow.com.au</span>
      </p>
    </div>
    <ul class="details">
      <li class="details__field">Name:</li>
      <li class="details__field">Procedure performed:</li>
      <li class="details__field">Date of procedure (month/year):</li>
      <li class="details__field">Treating clinic name:</li>
      <li class="details__field">Treating clinic signature:</li>
    </ul>
  </section>

  <section class="card card--front" aria-label="Card front: restaurant message">
    <div class="clinic-strip">
      <span class="clinic-strip__name">Bernard Whitlow</span>
      <span class="clinic-strip__dot"></span>
    </div>
    <ul class="message">
      <li class="message__point">The individual bearing this card has undergone weight loss surgery.</li>
      <li class="message__point">Around 500,000 of these procedures are performed around the world every year.</li>
      <li class="message__point">This surgery restricts portion sizes to between half and one cup of food at a time.</li>
      <li class="message__point">Please give consideration to allowing smaller portions of your regular meals to be ordered to reduce wastage and excess costs.</li>
      <li class="message__point">Example: a half size portion priced at two thirds of usual cost.</li>
    </ul>
  </section>
</body>
</html>
```